Business Card Design - Commercial Photographer

Professional Photographer requires eye catching creative business card. The design will need to incorporate my current logo in some form & not clash with my website tones & colours ( although website will be re designed in the future ). I'm currently shooting new folios in Commercial, Fashion & Architecture so I'm marketing to professional clients rather than portrait / wedding clients. Looking for something professional & creative.

Industry/Entity Type

Marketing

Requirements
Must have
• Website address - www.brightmarrowlens.com.au

Phone number - 0452786104

Email - info@brightmarrowlens.com.au

```html
<!DOCTYPE html>
<html lang="en">
<head>
<meta charset="utf-8">
<title>Reid Calloway – Photographer Business Card</title>
<link href="https://fonts.googleapis.com/css2?family=Open+Sans:wght@400;600;700&family=Libre+Baskerville&display=swap" rel="stylesheet">
<style>
  :root {
    --page-bg: #efece6;
    --frame: #231f20;
    --gold: #b39a6a;
    --white: #ffffff;
    --rec-red: #e0161b;
    --ink: #231f20;
  }
  html, body {
    margin: 0;
    padding: 0;
    width: 1200px;
    height: 913px;
    overflow: hidden;
    background: var(--page-bg);
    font-family: "Open Sans", Arial, sans-serif;
  }
  .business-card {
    position: absolute;
    left: 150px;
    top: 196px;
    width: 900px;
    height: 520px;
  }
  .card-frame {
    position: absolute;
    inset: 0;
  }
  .website {
    position: absolute;
    left: 60px;
    top: 16px;
    font-size: 26px;
    letter-spacing: 0.5px;
    color: var(--gold);
  }
  .rec-label {
    position: absolute;
    left: 64px;
    top: 84px;
    font-family: "Libre Baskerville", Georgia, serif;
    font-size: 22px;
    color: var(--ink);
    display: flex;
    align-items: center;
    gap: 6px;
  }
  .rec-dot {
    width: 16px;
    height: 16px;
    border-radius: 50%;
    background: var(--rec-red);
  }
  .identity {
    position: absolute;
    left: 60px;
    top: 438px;
    line-height: 1;
  }
  .identity .name {
    font-size: 44px;
    font-weight: 700;
    color: var(--white);
  }
  .identity .role {
    font-size: 24px;
    color: var(--gold);
    margin-top: 2px;
  }
  .contact {
    position: absolute;
    right: 40px;
    top: 402px;
    text-align: right;
    font-size: 22px;
    line-height: 1.3;
    color: var(--white);
  }
  .contact .label {
    color: var(--gold);
  }
</style>
</head>
<body>
  <div class="business-card">
    <svg class="card-frame" width="900" height="520" viewBox="0 0 900 520">
      <!-- viewfinder frame -->
      <path fill="var(--frame)" fill-rule="evenodd"
        d="M40 0 H860 A40 40 0 0 1 900 40 V480 A40 40 0 0 1 860 520 H40 A40 40 0 0 1 0 480 V40 A40 40 0 0 1 40 0 Z
           M44 70 H856 V390 H44 Z"/>
      <!-- focus brackets -->
      <g class="focus-brackets" fill="none" stroke="var(--ink)" stroke-width="2">
        <path d="M380 190 V160 H410"/>
        <path d="M490 160 H520 V190"/>
        <path d="M520 270 V300 H490"/>
        <path d="M410 300 H380 V270"/>
      </g>
      <!-- status icons -->
      <g class="icon-exposure" fill="none" stroke="var(--ink)" stroke-width="2">
        <circle cx="742" cy="100" r="7"/>
        <path d="M742 85v5M742 110v5M727 100h5M752 100h5M731 89l4 4M749 107l4 4M731 111l4-4M749 93l4-4"/>
      </g>
      <g class="icon-battery">
        <rect x="776" y="88" width="36" height="20" rx="3" fill="none" stroke="var(--ink)" stroke-width="2.5"/>
        <rect x="812" y="94" width="4" height="8" fill="var(--ink)"/>
        <rect x="780" y="92" width="28" height="12" fill="var(--ink)"/>
      </g>
      <path class="icon-flash" d="M828 112 l-10 16 h8 l-4 14 l12 -18 h-8 l6 -12 z" fill="var(--ink)"/>
      <!-- speaker icon -->
      <g class="icon-speaker" fill="var(--white)">
        <path d="M62 402 h8 l10 -8 v26 l-10 -8 h-8 z"/>
        <path d="M86 400 q6 7 0 14 M91 396 q10 11 0 22" fill="none" stroke="var(--white)" stroke-width="2"/>
      </g>
    </svg>

    <div class="website">www.brightmarrowlens.com.au</div>
    <div class="rec-label">Rec<span class="rec-dot"></span></div>

    <div class="identity">
      <div class="name">Reid Calloway</div>
      <div class="role">photographer</div>
    </div>

    <div class="contact">
      <div><span class="label">Email:</span> info@brightmarrowlens.com.au</div>
      <div><span class="label">Phone:</span> 0452 786 104</div>
    </div>
  </div>
</body>
</html>
```